gka 2014 bcard design

We have a new logo that we have yet to incorporate into any of our materials. We are under the gun to get new business cards done as soon as possible. This is our 20th year in business and we specialize in providing entertainment and audio-visual services for private and corporate events. Please see our website for more www.goldkiteacts.com
Being that we're in the entertainment industry, our "look" can be somewhat edgy and risky, but at the same time not "over the top". In fact, we would probably lean to a "less is more" style.
One side of the card should have our contact information for phones, email and address, and the other should have our slogan "celebrate, motivate, fascinate". We also want Facebook and Instagram (goldkiteactsevents) there as well, but not sure if it should be on back or front.
Target Market(s)
High net worth individuals, creative types in both the corporate and social markets
Industry/Entity Type
Entertainment
Look and feel

```html
<!DOCTYPE html>
<html lang="en">
<head>
<meta charset="utf-8">
<title>gka business card</title>
<link rel="stylesheet" href="https://fonts.googleapis.com/css2?family=Questrial&display=swap">
<style>
  :root {
    --stage: #e8e8e8;
    --crop: #333333;
    --card-black: #000000;
    --card-coral: #f2705d;
    --ink-light: #ffffff;
    --accent: #f2705d;
  }
  html, body {
    margin: 0;
    padding: 0;
    overflow: hidden;
  }
  body {
    width: 1200px;
    height: 900px;
    background: var(--stage);
    font-family: "Questrial", sans-serif;
    color: var(--ink-light);
    position: relative;
  }
  .crop-marks {
    position: absolute;
    left: 0;
    top: 0;
  }
  .card {
    position: absolute;
    left: 246px;
    width: 700px;
    height: 350px;
    border-radius: 15px;
    box-sizing: border-box;
  }
  .card--front {
    top: 57px;
    background: var(--card-black);
    text-align: center;
  }
  .card--back {
    top: 494px;
    background: var(--card-coral);
  }
  .brand-mark {
    position: absolute;
    left: 300px;
    top: 40px;
    width: 100px;
    height: 100px;
    border-radius: 50%;
    background: var(--accent);
  }
  .brand-name {
    position: absolute;
    left: 0;
    right: 0;
    top: 152px;
    margin: 0;
    font-size: 33px;
    font-weight: 400;
    letter-spacing: 0.5px;
    line-height: 1;
  }
  .brand-descriptor {
    position: absolute;
    left: 0;
    right: 0;
    top: 197px;
    margin: 0;
    font-size: 15px;
    letter-spacing: 3.5px;
    line-height: 21px;
    text-transform: uppercase;
  }
  .tagline {
    position: absolute;
    left: 0;
    right: 0;
    top: 282px;
    margin: 0;
    font-size: 28px;
    letter-spacing: 4.5px;
    line-height: 1;
  }
  .contact {
    position: absolute;
    left: 69px;
    top: 53px;
  }
  .contact__name {
    margin: 0;
    font-size: 28px;
    font-weight: 400;
    line-height: 1;
  }
  .contact__title {
    margin: 2px 0 0;
    font-size: 19px;
    line-height: 1;
  }
  .contact__details {
    position: absolute;
    left: 69px;
    top: 158px;
    margin: 0;
    font-style: normal;
    font-size: 17px;
    line-height: 23.5px;
  }
  .contact__social {
    position: absolute;
    left: 69px;
    top: 292px;
    display: flex;
    align-items: center;
    gap: 8px;
    font-size: 16.5px;
    line-height: 1;
  }
  .contact__social-dot {
    width: 16px;
    height: 16px;
    border-radius: 50%;
    background: var(--ink-light);
  }
</style>
</head>
<body>
  <svg class="crop-marks" width="1200" height="900" viewBox="0 0 1200 900" aria-hidden="true">
    <g stroke="var(--crop)" stroke-width="1" fill="none">
      <path d="M218 57H245M245 18V57"/>
      <path d="M975 57H948M948 18V57"/>
      <path d="M218 407H245M245 407V446"/>
      <path d="M975 407H948M948 407V446"/>
      <path d="M218 494H245M245 453V494"/>
      <path d="M975 494H948M948 453V494"/>
      <path d="M218 843H245M245 843V882"/>
      <path d="M975 843H948M948 843V882"/>
    </g>
  </svg>

  <section class="card card--front">
    <div class="brand-mark" aria-hidden="true"></div>
    <h1 class="brand-name">gold kite acts</h1>
    <p class="brand-descriptor">Events &amp;<br>Entertainment</p>
    <p class="tagline">celebrate · motivate · fascinate</p>
  </section>

  <section class="card card--back">
    <div class="contact">
      <h2 class="contact__name">Daniel Marsh</h2>
      <p class="contact__title">title here</p>
    </div>
    <address class="contact__details">
      418 Harlow Street, 4th Floor<br>
      New York, NY 10001<br>
      T | 212-555-0148<br>
      E | daniel@goldkiteacts.com<br>
      W | www.goldkiteacts.com
    </address>
    <div class="contact__social">
      <span class="contact__social-dot" aria-hidden="true"></span>
      <span>goldkiteactsevents</span>
    </div>
  </section>
</body>
</html>
```